Mail order Nursery needs banner for promoting perennials that compliment roses.

banner should be 1135 wide x165 tall. We have an existing one displayed but we are not happy with the way it is washed out. Use your creativity to give us something that pops. Would love to see some watercolor or some other form of image other than just words washed across a stock photo. Banner needs to read Perennial Companions for Roses or some variation of that. Colors need to compliment our current theme. You can view the page and banner I want to replace at www.meadowlarkbloomyard.com. The banner we want to replace has been uploaded to the pixel forum file drop box. Thanks for your help and I look forward to seeing what you guys come up with. EDIT: I don't think I was clear enough in by brief. This banner promotes the sale of plants that look good planted with roses. We are getting to many submissions that are using only roses as the backdrop. We are looking for different types of plants that you would grow in your garden to compliment your roses. Thanks for all your hard work.

Target Market(s)

Home owners between 30 and 65

Industry/Entity Type

Nursery

Colors
33a6d7
e667a6

Requirements
Must have
• Text promotion perennials that compliment roses.... does not have to be those exact words but get the point across
Should not have
• Stock Photos with simple text washed across it.

```html
<!DOCTYPE html>
<html lang="en">
<head>
<meta charset="utf-8">
<title>Perennial Companions for Roses</title>
<link rel="stylesheet" href="https://fonts.googleapis.com/css2?family=Kaushan+Script&display=swap">
<style>
  :root {
    --lawn-green: #6f8a5a;
    --foliage-dark: #3f5a36;
    --rose-pink: #e08fc4;
    --rose-light: #f3c6e2;
    --bloom-white: #f4f4ef;
    --inset-violet: #b0258e;
    --inset-leaf: #4d7a2e;
    --inset-cream: #e8f0c8;
    --title-yellow: #ffef1a;
    --title-outline: #2a2410;
    --frame-yellow: #ffe81c;
  }
  html, body {
    margin: 0;
    padding: 0;
    width: 1200px;
    height: 174px;
    overflow: hidden;
    background: #ffffff;
  }
  .banner {
    position: relative;
    width: 1200px;
    height: 174px;
    overflow: hidden;
  }
  .garden-backdrop {
    position: absolute;
    inset: 0;
    background:
      radial-gradient(ellipse 220px 90px at 850px 70px, var(--bloom-white) 0%, rgba(244,244,239,0) 100%),
      radial-gradient(ellipse 300px 70px at 520px 165px, var(--rose-light) 0%, rgba(243,198,226,0) 100%),
      radial-gradient(ellipse 260px 70px at 300px 130px, var(--rose-pink) 0%, rgba(224,143,196,0) 100%),
      linear-gradient(180deg, var(--lawn-green) 0%, var(--foliage-dark) 40%, #8a7a86 70%, var(--rose-pink) 100%);
  }
  .flower-inset {
    position: absolute;
    left: 0;
    top: 0;
    width: 240px;
    height: 174px;
  }
  .banner-title {
    position: absolute;
    left: 258px;
    top: 30px;
    margin: 0;
    font-family: "Kaushan Script", cursive;
    font-weight: 400;
    font-size: 68px;
    line-height: 1;
    letter-spacing: 1px;
    white-space: nowrap;
    color: var(--title-yellow);
    -webkit-text-stroke: 1.5px var(--title-outline);
    text-shadow: 2px 3px 3px rgba(0,0,0,0.55);
  }
</style>
</head>
<body>
  <div class="banner">
    <div class="garden-backdrop" role="img" aria-label="Photograph of a rose garden with beds of pink and white roses, trees and lawn behind"></div>

    <svg class="flower-inset" viewBox="0 0 240 174" xmlns="http://www.w3.org/2000/svg">
      <defs>
        <radialGradient id="insetBlooms" cx="0.45" cy="0.55" r="0.7">
          <stop offset="0" stop-color="var(--inset-violet)"/>
          <stop offset="0.35" stop-color="var(--inset-leaf)"/>
          <stop offset="0.75" stop-color="var(--inset-cream)"/>
          <stop offset="1" stop-color="var(--inset-leaf)"/>
        </radialGradient>
      </defs>
      <g role="img" aria-label="Close-up photograph of a magenta rugosa rose among white snowball viburnum blooms">
        <ellipse cx="95" cy="87" rx="128" ry="112" fill="url(#insetBlooms)"/>
      </g>
      <ellipse class="inset-frame" cx="95" cy="87" rx="128" ry="112" fill="none" stroke="var(--frame-yellow)" stroke-width="4"/>
    </svg>

    <h1 class="banner-title">Perennial Companions for Roses</h1>
  </div>
</body>
</html>
```